Redesign Call Answering Service Company Website

There is a good explanation of what we do at existing website hummingdesk.com.au.

We are getting traffic and now want to increase conversions and reduce drop offs. We need to create trust very quickly.

Once website done we will be looking to redesign logo.

We want to use “F” shaped reading pattern for website viewers. 2 very rough ideas on attached wireframes docs. The winning site only needs to follow the rough layout – no need for boxes, etc. Looking for creative help here!

One page needed (home page) that easily becomes all other pages without a "price reference" (see wire frames).

All existing pages will have new/updated content added with extra pages added.

Target Market(s)

Target market to appeal to is 70% females 25 to 60, self-employed business owners, complimentary/alternative therapists, small to medium business ente

Industry/Entity Type

It Company

Requirements
Must have
• must have items on wire frames
must have a Client Login (to self-service area)
must have a Contact Area with 4 x phone numbers, 1 x fax number and email/contact us

```html
<!DOCTYPE html>
<html lang="en">
<head>
<meta charset="utf-8">
<title>Humming Desk – Call Answering</title>
<link href="https://fonts.googleapis.com/css2?family=Jost:wght@400;500;600&family=Yanone+Kaffeesatz:wght@300;400&family=Arimo:wght@400;700&display=swap" rel="stylesheet">
<style>
:root{
  --brown:#8a6a4f;
  --teal:#4fb3b0;
  --navy:#1d4f7a;
  --blue:#4e86b5;
  --yellow:#e3c23c;
  --green:#8aab2d;
  --pink:#f4d9d3;
  --cream:#fbf0c3;
  --dark:#2e2e2e;
  --ink:#333;
}
*{margin:0;padding:0;box-sizing:border-box}
html,body{width:1200px;height:954px;overflow:hidden}
body{position:relative;background:linear-gradient(#e4dcc2 0,#f4f0e4 150px,#fff 420px);font-family:'Jost',sans-serif;color:var(--ink)}
.abs{position:absolute}
.cond{font-family:'Yanone Kaffeesatz',sans-serif}

.brand{left:26px;top:60px;display:flex;align-items:center;gap:10px}
.brand-dot{width:40px;height:40px;border-radius:50%;background:#f08a2c}
.brand-name{font-size:26px;font-weight:500;color:var(--blue)}

.badge{left:600px;top:6px;width:68px;height:68px;border-radius:50%;background:#e3efe8;border:2px solid #b9cfc6;display:flex;align-items:center;justify-content:center}
.slogan{left:680px;top:2px;width:262px;text-align:center;color:var(--brown)}
.slogan h1{font-size:43px;font-weight:600;line-height:46px}
.slogan h2{font-size:22px;font-weight:600;line-height:20px;color:#7a5532}
.slogan p{font-family:'Yanone Kaffeesatz',sans-serif;font-size:19px;color:#444;line-height:22px}

.nav{left:218px;top:92px;width:724px;height:37px;background:linear-gradient(#fff,#eee);border:1px solid #d7d7d7;box-shadow:0 2px 3px rgba(0,0,0,.2);display:flex;align-items:center;justify-content:space-around;font-size:16px;color:#555;letter-spacing:.5px}
.nav span.sep{color:#777}

.login-tab{left:966px;top:38px;width:114px;height:28px;background:#f5d9c8;border-radius:8px 8px 0 0;font-family:'Yanone Kaffeesatz',sans-serif;font-size:19px;color:#7a5a48;display:flex;align-items:center;gap:6px;padding-left:8px}
.login{left:955px;top:64px;width:230px;height:68px;background:#fbeee2;border:2px solid #f0d7c6;border-radius:8px}
.login .field{position:absolute;left:13px;width:142px;height:25px;background:#fff;border:1px solid #e2cdbd;font-size:11px;color:#999;padding:5px 6px;font-family:Arimo,sans-serif}
.login .btn{position:absolute;left:166px;top:22px;width:48px;height:25px;border-radius:12px;background:linear-gradient(#fafafa,#ddd);font-size:12px;color:#555;display:flex;align-items:center;justify-content:center;font-family:Arimo,sans-serif}

.hero{left:26px;top:157px;width:758px;height:280px;background:linear-gradient(90deg,#f3f8fb 0,#e4f1f8 45%,#cfe4ef 60%,#e9eef0 100%);overflow:hidden}
.hero-photo{position:absolute;left:430px;top:0;width:328px;height:280px;background:linear-gradient(90deg,rgba(230,240,245,0),#d8d0c8 40%,#3a2a22 75%,#e8e6e4 100%)}
.hero-icon{position:absolute;left:24px;top:9px;width:48px;height:48px;border-radius:50%;border:3px solid #888;display:flex;align-items:center;justify-content:center}
.hero .welcome{position:absolute;left:79px;top:6px;font-size:26px;color:#555;font-family:'Yanone Kaffeesatz',sans-serif;font-weight:300}
.hero .title{position:absolute;left:79px;top:30px;font-size:27px;font-weight:600;color:var(--teal)}
.hero .title b{color:var(--brown);font-weight:600}
.hero ul{position:absolute;left:26px;top:64px;list-style:none;font-family:'Yanone Kaffeesatz',sans-serif;font-size:18px;color:var(--navy);line-height:21px}
.hero li{margin-bottom:11px;padding-left:12px;position:relative}
.hero li:before{content:"";position:absolute;left:0;top:8px;width:5px;height:5px;border-radius:50%;background:var(--navy)}

.price{left:788px;top:157px;width:397px;height:76px;background:var(--yellow);color:#fff;padding-left:13px}
.price p{font-family:'Yanone Kaffeesatz',sans-serif;font-size:21px;font-weight:300;margin-top:5px;line-height:22px;padding-left:4px}
.price h3{font-size:41px;font-weight:600;line-height:44px}
.trial{left:788px;top:236px;width:397px;height:162px;background:linear-gradient(#f2d2cc,#faece8)}
.trial-box{position:absolute;left:17px;top:7px;width:103px;height:155px;background:linear-gradient(100deg,#2c6fb8,#7fb2de 60%,#e4eef6)}
.trial h3{position:absolute;left:136px;top:10px;font-size:40px;font-weight:600;color:var(--brown)}
.trial p{position:absolute;left:136px;top:55px;width:252px;font-family:'Yanone Kaffeesatz',sans-serif;font-size:17px;line-height:18px;color:#333}
.pill{position:absolute;left:136px;top:119px;width:106px;height:21px;border-radius:11px;background:linear-gradient(#b08f74,#7d6149);color:#fff;font-size:13px;font-weight:600;display:flex;align-items:center;justify-content:center}
.plans{left:788px;top:398px;width:397px;height:39px;background:var(--green);color:#fff;display:flex;align-items:center;justify-content:space-between;padding:0 13px 0 12px}
.plans h3{font-size:25px;font-weight:500}
.plans span{font-family:'Yanone Kaffeesatz',sans-serif;font-size:20px}

.video{left:28px;top:454px;width:424px;height:298px;background:#fff;box-shadow:0 0 4px rgba(0,0,0,.3)}
.screen{position:absolute;left:7px;top:7px;width:410px;height:284px;background:#d3dde1}
.play-big{position:absolute;left:207px;top:121px;width:40px;height:40px;background:#2f2f2f;border-radius:3px}
.play-small{position:absolute;left:9px;top:234px;width:60px;height:40px;background:#2f2f2f;border-radius:3px}
.bar{position:absolute;left:79px;top:244px;width:321px;height:30px;background:#2f2f2f;border-radius:3px;color:#fff;font-size:10px;font-family:Arimo,sans-serif}
.bar .t{position:absolute;left:9px;top:9px}
.bar .track{position:absolute;left:45px;top:10px;width:190px;height:10px;border:1px solid #ddd}
.bar .vol{position:absolute;left:243px;top:10px;width:46px;height:10px;background:repeating-linear-gradient(90deg,#fff 0 3px,transparent 3px 5px)}

.links{left:470px;top:458px;width:275px;list-style:none}
.links li{height:29px;background:linear-gradient(90deg,#fff 0,#e8ecd8 50%,#d5ddb4 100%);border-bottom:2px solid #fff;font-size:15px;color:#333;padding:4px 0 0 16px;position:relative}
.links li:before{content:"";position:absolute;left:18px;top:10px;border-left:5px solid #333;border-top:4px solid transparent;border-bottom:4px solid transparent}
.links li{padding-left:28px}
.refund{left:745px;top:452px;width:35px;height:296px;background:var(--green)}
.refund span{position:absolute;left:35px;top:28px;transform:rotate(90deg);transform-origin:0 0;white-space:nowrap;color:#fff;font-size:23px;font-weight:600}

.company{left:28px;top:782px;width:753px;height:100px;display:flex;box-shadow:0 0 3px rgba(0,0,0,.25)}
.co-mark{width:131px;background:linear-gradient(#f7f7f7,#dcdcdc);display:flex;flex-direction:column;align-items:center;justify-content:center;gap:4px}
.co-mark i{width:26px;height:26px;border-radius:50%;background:#f08a2c}
.co-mark span{font-size:14px;font-weight:500;color:var(--blue)}
.co-info{width:369px;background:var(--yellow);border-left:2px solid #fff;border-right:2px solid #fff;text-align:center;font-family:Arimo,sans-serif;font-size:17px;line-height:21px;color:#1a1a1a;padding-top:7px}
.co-info b{font-size:19px}
.co-photo{flex:1;background:linear-gradient(#fafafa,#dedede);display:flex;align-items:center;justify-content:center;text-align:center;font-family:'Yanone Kaffeesatz',sans-serif;font-size:17px;color:#888;line-height:24px}

.side{left:788px;top:452px;width:397px;height:431px;background:linear-gradient(#fffefa,var(--cream))}
.item{position:absolute;left:0;width:397px;height:80px}
.item .ico{position:absolute;left:30px;top:0;width:64px;height:64px}
.item h4{position:absolute;font-size:19px;font-weight:500;color:var(--blue)}
.item a{position:absolute;font-family:'Yanone Kaffeesatz',sans-serif;font-size:21px;color:#333;text-decoration:underline}

.footer{left:0;top:898px;width:1200px;height:56px;background:var(--dark);color:#bbb;font-family:'Yanone Kaffeesatz',sans-serif;font-size:16px}
.footer .copy{position:absolute;left:30px;top:17px}
.footer nav{position:absolute;left:342px;top:16px;display:flex;gap:6px}
.social{position:absolute;top:15px;width:23px;height:23px;border-radius:2px}
</style>
</head>
<body>

<div class="abs brand"><i class="brand-dot"></i><span class="brand-name">Humming Desk</span></div>

<div class="abs badge">
  <svg width="30" height="40" viewBox="0 0 30 40"><rect x="3" y="1" width="24" height="38" rx="4" fill="#4fb3b0"/><rect x="7" y="6" width="16" height="11" fill="#dff3f1"/><g fill="#dff3f1"><circle cx="10" cy="23" r="2"/><circle cx="15" cy="23" r="2"/><circle cx="20" cy="23" r="2"/><circle cx="10" cy="29" r="2"/><circle cx="15" cy="29" r="2"/><circle cx="20" cy="29" r="2"/></g></svg>
</div>
<div class="abs slogan">
  <h1>Be Confident</h1>
  <h2>Your Calls are Answered</h2>
  <p>whatever you are doing</p>
</div>

<nav class="abs nav">
  <span>Home</span><span class="sep">|</span><span>Phone Answering</span><span class="sep">|</span><span>Virtual Reception</span><span class="sep">|</span><span>FAQ</span><span class="sep">|</span><span>About Us</span>
</nav>

<div class="abs login-tab">
  <svg width="16" height="18" viewBox="0 0 16 18"><circle cx="8" cy="5" r="4.5" fill="#8a6a4f"/><path d="M0 18c0-6 4-8 8-8s8 2 8 8z" fill="#8a6a4f"/></svg>
  CLIENT LOGIN
</div>
<div class="abs login">
  <div class="field" style="top:6px">user name</div>
  <div class="field" style="top:35px">password</div>
  <div class="btn">Login</div>
</div>

<section class="abs hero">
  <div class="hero-photo" role="img" aria-label="Photo of a smiling receptionist wearing a headset"></div>
  <div class="hero-icon">
    <svg width="26" height="26" viewBox="0 0 24 24"><path d="M6.6 10.8a15 15 0 006.6 6.6l2.2-2.2c.3-.3.7-.4 1-.2 1.1.4 2.3.6 3.6.6.6 0 1 .4 1 1V20c0 .6-.4 1-1 1A17 17 0 013 4c0-.6.4-1 1-1h3.5c.6 0 1 .4 1 1 0 1.3.2 2.5.6 3.6.1.3 0 .7-.2 1z" fill="#888"/></svg>
  </div>
  <div class="welcome">Welcome to</div>
  <div class="title">Humming <b>DESK</b></div>
  <ul>
    <li>Live phone answering by australian virtual receptionists</li>
    <li>Australian based professional receptionists will answer your phones customised<br>to your requirements</li>
    <li>HD deliver excellent phone based business support solutions using smart technologies</li>
    <li>Australian based team that cares about you, your business and your clients</li>
    <li>Customisable inbound call management solutions aimed at the SME market</li>
    <li>Complete range of cost effective services to support any business.</li>
  </ul>
</section>

<div class="abs price"><p>form as little as</p><h3>$4.90 per week</h3></div>
<div class="abs trial">
  <div class="trial-box" role="img" aria-label="Free trial product box illustration"></div>
  <h3>Free Trial</h3>
  <p>Lorem Ipsum is simply dummy text of the print-ing and typesetting industry Lorem Ipsum has been the industry's standard .</p>
  <div class="pill">View More ▸</div>
</div>
<div class="abs plans"><h3>Plans &amp; Pricing</h3><span>View More ▸</span></div>

<div class="abs video">
  <div class="screen">
    <div class="play-big"><svg width="40" height="40"><path d="M15 11l13 9-13 9z" fill="#fff"/></svg></div>
    <div class="play-small"><svg width="60" height="40"><path d="M24 11l15 9-15 9z" fill="#fff"/></svg></div>
    <div class="bar"><span class="t">00:00</span><span class="track"></span><span class="vol"></span>
      <svg class="abs" style="left:298px;top:8px" width="14" height="14"><path d="M1 5V1h4M9 1h4v4M13 9v4H9M5 13H1V9" stroke="#fff" stroke-width="2" fill="none"/></svg>
    </div>
  </div>
</div>

<ul class="abs links">
  <li>Product Links</li>
  <li>$1.90 per message</li>
  <li>Value Pack</li>
  <li>Virtual Switchboard</li>
  <li>Call cover when not available</li>
  <li>Complexs Services / Sales Scripts</li>
  <li>Inbound</li>
  <li>28 day prepay</li>
  <li>Plans to suit higher users</li>
  <li>Free 1300 Numbers</li>
</ul>
<div class="abs refund"><span>100% Refund Policy</span></div>

<div class="abs company">
  <div class="co-mark"><i></i><span>Humming Desk</span></div>
  <div class="co-info">
    <b>Humming Desk Pty Ltd</b><br>
    ABN: 51 208 337 914<br>
    Suite 4, 22 Elm St, Ryde, NSW 2112<br>
    info@hummingdesk.com.au
  </div>
  <div class="co-photo" role="img" aria-label="Office building photo">Office Building Image<br>Will come here</div>
</div>

<aside class="abs side">
  <div class="item" style="top:0">
    <div class="ico" role="img" aria-label="Rating checklist illustration" style="top:0;left:20px;width:80px;height:72px;background:linear-gradient(135deg,#f6e3dc,#dde8f3)"></div>
    <h4 style="left:127px;top:8px">Customer Testimonials</h4>
    <a style="left:127px;top:32px">Click Here</a>
  </div>
  <div class="item" style="top:95px">
    <svg class="ico" viewBox="0 0 64 64"><circle cx="32" cy="32" r="29" fill="#2f97d6" stroke="#d9dde0" stroke-width="4"/><text x="32" y="44" text-anchor="middle" font-family="Arimo,sans-serif" font-size="34" font-weight="700" fill="#fff">?</text></svg>
    <h4 style="left:131px;top:8px">Ask a Question</h4>
    <a style="left:131px;top:32px">Click Here</a>
  </div>
  <div class="item" style="top:178px">
    <div class="ico" role="img" aria-label="Newspaper character illustration" style="left:22px;width:78px;height:76px;background:linear-gradient(#f2f2f2,#f0b43a)"></div>
    <h4 style="left:128px;top:8px">Latest News</h4>
    <a style="left:128px;top:32px">Click Here</a>
  </div>
  <div class="item" style="top:278px">
    <div class="ico" style="left:42px;top:2px;width:50px;height:50px;border-radius:8px;background:#f57d00"></div>
    <h4 style="left:128px;top:0">Blog</h4>
    <a style="left:128px;top:24px">Click Here</a>
  </div>
  <div class="item" style="top:360px">
    <svg class="ico" style="left:38px;top:0;width:54px;height:58px" viewBox="0 0 54 58"><ellipse cx="27" cy="50" rx="22" ry="6" fill="#333"/><path d="M6 28l12 14L48 4" stroke="#c81a1a" stroke-width="8" fill="none" stroke-linecap="round"/></svg>
    <h4 style="left:124px;top:3px">Answer a 1 Question Survey</h4>
    <a style="left:124px;top:27px">Click Here</a>
  </div>
</aside>

<footer class="abs footer">
  <span class="copy">Copyright@2012 Humming Desk Pty Ltd</span>
  <nav><span>Home</span>|<span>Phone Answering</span>|<span>Diary Management</span>|<span>Service Desk</span>|<span>Plans &amp; Pricing</span>|<span>FAQ</span>|<span>About Us</span>|<span>Contact Us</span></nav>
  <span class="social" style="left:1128px;background:#3b5998"></span>
  <span class="social" style="left:1160px;background:#33b5e5"></span>
</footer>

</body>
</html>
```